Executive Performance Review mapped on J-curve

I need to turn an executive company performance review into a visual infographic. The list of accomplishments is grouped into four calendar quarters. Each quarter needs a subtle representation of the season. The four quarters and associated list of accomplishments need to be mapped to a J-curve. - Spreadsheet with accomplishments attached (Throughput)- Sample image of a J-curve. You can google J-curve to see more images.- The title should be "Dorna Pelsketh Year in Review"

Target Market(s)

Board of Directors

Requirements
Nice to have
• This will be presented to a company founder that is an artist and customer experience expert. He is very visual so a nice visual representation of the data will be impactful. He also uses the phrase that you have to live with or work with someone for four seasons before you really know them. This is why I have the seasons mapped to the quarters. The Fall season motif should be gloomy and stormy.

```html
<!DOCTYPE html>
<html lang="en">
<head>
<meta charset="utf-8">
<title>J-curve Performance Review</title>
<link href="https://fonts.googleapis.com/css2?family=Lilita+One&family=Oswald:wght@500;600&family=Signika:wght@400;500&family=Open+Sans:wght@400&display=swap" rel="stylesheet">
<style>
  :root {
    --sky: #a8d2f5;
    --grid: #8fbde6;
    --grid-label: #7aa9d2;
    --title-red: #e8412f;
    --accent-green: #27a35c;
    --curve-green: #17a34a;
    --ink: #1c1c1c;
    --dot-red: #e53a2c;
    --white: #ffffff;
  }
  * { margin: 0; padding: 0; box-sizing: border-box; }
  html, body { width: 781px; height: 1200px; overflow: hidden; }
  body { background: var(--sky); position: relative; font-family: "Open Sans", sans-serif; color: var(--ink); }

  .chart { position: absolute; left: 0; top: 0; width: 781px; height: 1200px; }

  .review-title {
    position: absolute; left: 70px; top: 28px;
    font-family: "Lilita One", sans-serif; font-weight: 400;
    font-size: 40px; letter-spacing: 1px; color: var(--title-red);
  }

  .quarter { position: absolute; width: 230px; }
  .quarter--summer { left: 70px; top: 90px; }
  .quarter--fall { left: 297px; top: 90px; }
  .quarter--spring { left: 506px; top: 90px; }
  .quarter--winter { left: 297px; top: 538px; }

  .quarter-head { display: flex; align-items: flex-start; gap: 10px; height: 54px; }
  .season-name {
    font-family: "Oswald", sans-serif; font-weight: 600;
    font-size: 27px; line-height: 27px; color: var(--ink); text-transform: uppercase;
  }
  .season-period {
    font-family: "Oswald", sans-serif; font-weight: 500;
    font-size: 18px; line-height: 20px; color: var(--ink);
  }
  .season-motif { width: 46px; height: 40px; border-radius: 8px; margin-top: 2px; }
  .season-motif--summer { background: linear-gradient(135deg, #4cbd7c, #2aa35d); }
  .season-motif--fall { background: linear-gradient(180deg, #3ba968, #218f4d); border-radius: 20px 20px 8px 8px; }
  .season-motif--spring { background: linear-gradient(180deg, #55c286, #2a9d5a); border-radius: 20px 20px 6px 6px; }
  .season-motif--winter { background: linear-gradient(180deg, #4ab87a, #2a9a58); border-radius: 20px 20px 8px 8px; }

  .section-title {
    font-family: "Signika", sans-serif; font-weight: 500;
    font-size: 17px; color: var(--accent-green);
    margin-top: 6px; margin-bottom: 3px;
  }
  .section-list { list-style: none; font-size: 11.5px; line-height: 15.5px; }
  .section-list .gap { margin-top: 9px; }
</style>
</head>
<body>

<svg class="chart" viewBox="0 0 781 1200" aria-hidden="true">
  <g stroke="var(--grid)" stroke-width="1">
    <line x1="75" y1="760" x2="75" y2="1125"/><line x1="132" y1="760" x2="132" y2="1125"/>
    <line x1="190" y1="760" x2="190" y2="1125"/><line x1="247" y1="760" x2="247" y2="1125"/>
    <line x1="305" y1="760" x2="305" y2="1125"/><line x1="362" y1="760" x2="362" y2="1125"/>
    <line x1="419" y1="760" x2="419" y2="1125"/><line x1="477" y1="760" x2="477" y2="1125"/>
    <line x1="534" y1="760" x2="534" y2="1125"/><line x1="592" y1="760" x2="592" y2="1125"/>
    <line x1="649" y1="760" x2="649" y2="1125"/><line x1="706" y1="760" x2="706" y2="1125"/>
    <line x1="40" y1="1125" x2="781" y2="1125"/><line x1="40" y1="1069" x2="781" y2="1069"/>
    <line x1="40" y1="1013" x2="781" y2="1013"/><line x1="40" y1="957" x2="781" y2="957"/>
    <line x1="40" y1="901" x2="781" y2="901"/><line x1="40" y1="845" x2="781" y2="845"/>
    <line x1="40" y1="789" x2="781" y2="789"/>
  </g>
  <g font-family="Open Sans, sans-serif" font-size="13" fill="var(--grid-label)">
    <text x="66" y="1069">1</text><text x="66" y="1013">2</text><text x="66" y="957">3</text>
    <text x="66" y="901">4</text><text x="66" y="845">5</text><text x="66" y="789">6</text>
    <text x="58" y="1145">0</text><text x="128" y="1145">1</text><text x="186" y="1145">2</text>
    <text x="243" y="1145">3</text><text x="301" y="1145">4</text><text x="358" y="1145">5</text>
    <text x="415" y="1145">6</text><text x="473" y="1145">7</text><text x="530" y="1145">8</text>
    <text x="588" y="1145">9</text><text x="641" y="1145">10</text><text x="699" y="1145">11</text>
  </g>
  <path d="M39 942 C 120 1010, 190 1060, 281 1052 C 380 1045, 470 1010, 536 980 C 620 940, 700 880, 769 752"
        fill="none" stroke="var(--curve-green)" stroke-width="6" stroke-linecap="round"/>
  <g fill="var(--white)" stroke="var(--dot-red)" stroke-width="6">
    <circle cx="81" cy="980" r="12"/><circle cx="281" cy="1051" r="12"/>
    <circle cx="536" cy="980" r="12"/><circle cx="711" cy="791" r="12"/>
  </g>
  <circle cx="78" cy="1122" r="9" fill="var(--dot-red)"/>
  <g font-family="Signika, sans-serif" font-size="13" font-weight="500" fill="var(--title-red)">
    <text x="93" y="1108">Summer</text><text x="254" y="1108">Fall</text>
    <text x="528" y="1108">Winter</text><text x="694" y="1108">Spring</text>
  </g>
</svg>

<h1 class="review-title">J-curve Performance Review</h1>

<section class="quarter quarter--summer">
  <div class="quarter-head">
    <div><div class="season-name">Summer</div><div class="season-period">Q3 2018</div></div>
    <div class="season-motif season-motif--summer" role="img" aria-label="Summer motif: sun and beach umbrella"></div>
  </div>
  <h2 class="section-title">Transitions</h2>
  <ul class="section-list">
    <li>RO Transition from Reed &amp; Mila</li>
    <li>Start CR Office Initiative</li>
    <li>Tactical Ops transition from Reed</li>
    <li>Formalize Exec Team</li>
  </ul>
  <h2 class="section-title">Biz Architecture</h2>
  <ul class="section-list">
    <li>Independent Financial Audit</li>
    <li>Organizational Audit - Structure</li>
    <li>Organizational Audit - People</li>
    <li>XF Framework - ESU</li>
    <li class="gap">Defined Utilization, Realization,</li>
    <li>Availability</li>
  </ul>
  <h2 class="section-title">Strategy</h2>
  <ul class="section-list">
    <li>Effective Strategy Meeting</li>
    <li class="gap">Strategic Themes 2018 - 2020:</li>
    <li>Stablize, Accelerate, Surge</li>
    <li class="gap">Business Drivers: Drive Revenue,</li>
    <li>Improve Norvane Experience,</li>
    <li>Increase Brand Awareness</li>
  </ul>
  <h2 class="section-title">Sales</h2>
  <ul class="section-list">
    <li>Halverton Account Transition</li>
    <li class="gap">QVN Account Transition</li>
    <li class="gap">2 year Managed Services</li>
    <li>Engagement Model</li>
  </ul>
  <h2 class="section-title">Revenue / EBITA</h2>
  <ul class="section-list"><li>TBD</li></ul>
</section>

<section class="quarter quarter--fall">
  <div class="quarter-head">
    <div><div class="season-name">Fall</div><div class="season-period">Q4 2018</div></div>
    <div class="season-motif season-motif--fall" role="img" aria-label="Fall motif: storm cloud with rain and lightning"></div>
  </div>
  <h2 class="section-title">Biz Architecture</h2>
  <ul class="section-list">
    <li>XF Framework - Functional</li>
    <li>Meetings &amp; Scrum of Scrums</li>
    <li>Structured Reorg</li>
    <li>Implemented Reorg</li>
    <li>Quarterly Org Iteration cadence</li>
    <li>Defined Key Hire Plan</li>
    <li>CR Office Operational</li>
    <li>Time Accountability</li>
    <li>Tools ReConfig</li>
    <li>Org Structure v1</li>
  </ul>
  <h2 class="section-title">Strategy</h2>
  <ul class="section-list"><li>Internal QBR Accountability</li></ul>
  <h2 class="section-title">Sales</h2>
  <ul class="section-list"><li>Tarrant QBR</li><li>Halverton QBR</li></ul>
  <h2 class="section-title">Revenue / EBITA</h2>
  <ul class="section-list"><li>TBD</li></ul>
</section>

<section class="quarter quarter--spring">
  <div class="quarter-head">
    <div><div class="season-name">Spring</div><div class="season-period">Q2 2019</div></div>
    <div class="season-motif season-motif--spring" role="img" aria-label="Spring motif: blooming flower"></div>
  </div>
  <h2 class="section-title">Biz Architecture</h2>
  <ul class="section-list">
    <li>Tiered Pricing Pre-Paid Engagement Model</li>
    <li>XF Framework - Ideation Board</li>
    <li>Consulting Levels &amp; Salary Bands</li>
    <li>Roles &amp; Responsibilities</li>
  </ul>
  <h2 class="section-title">Key Hires</h2>
  <ul class="section-list">
    <li>Interim HR</li>
    <li>Provisional Client Partner</li>
    <li>Acting Director 1</li>
    <li>Acting Director 2</li>
    <li>Client Partner 1</li>
    <li>Sales Exec 1</li>
  </ul>
  <h2 class="section-title">Sales</h2>
  <ul class="section-list">
    <li>Opened BrightLane Door</li>
    <li>Flipped focus from operationaly run company</li>
    <li>to sales/marketing driven org</li>
    <li>KVT Direct</li>
  </ul>
  <h2 class="section-title">Revenue / EBITA</h2>
  <ul class="section-list"><li>TBD</li></ul>
</section>

<section class="quarter quarter--winter">
  <div class="quarter-head">
    <div><div class="season-name">Winter</div><div class="season-period">Q1 2019</div></div>
    <div class="season-motif season-motif--winter" role="img" aria-label="Winter motif: cloud with falling snow"></div>
  </div>
  <h2 class="section-title">Biz Architecture</h2>
  <ul class="section-list">
    <li>XF Framework - Progress</li>
    <li>Demos &nbsp;Org Structure - COE's</li>
    <li>Stablize Accounting &amp; Finance</li>
    <li>Exec Hiring Process</li>
  </ul>
  <h2 class="section-title">Key Hires</h2>
  <ul class="section-list"><li>Controller</li><li>Director CX</li></ul>
  <h2 class="section-title">Strategy</h2>
  <ul class="section-list">
    <li>Founders removed from front</li>
    <li>line activity Vantor QBR - Goal</li>
    <li>Setting &amp; Tracking</li>
  </ul>
  <h2 class="section-title">Sales</h2>
  <ul class="section-list"><li>QVN QBR</li><li>Halverton QBR</li></ul>
  <h2 class="section-title">Revenue / EBITA</h2>
  <ul class="section-list"><li>TBD</li></ul>
</section>

</body>
</html>
```